New Flyer Design Project

I would like to purchase a customized version of a design you have previously submitted - https://www.artmarketly.com/design/58210947
hi
would like the design about the some. just with our  details and logo
office number 01394528160
Mobil number 07821563047
web lunarsweep.ltd
email lunarsweep@postmerin.co.uk
on the back we would like to put a price list

```html
<!DOCTYPE html>
<html lang="en">
<head>
<meta charset="utf-8">
<title>Lunar Sweep Flyer</title>
<link href="https://fonts.googleapis.com/css2?family=Montserrat:wght@400;500;600;700;800;900&family=Anton&display=swap" rel="stylesheet">
<style>
  :root {
    --stage: #d6d6d6;
    --paper: #ffffff;
    --brand-blue: #1f6fc4;
    --deep-blue: #0d4f9e;
    --navy: #163d7a;
    --sky: #3fc4f2;
    --pink: #e3238f;
    --ink: #222222;
    --charcoal: #2b2b2b;
    --pill-grey: #c9c9c9;
    --row-a: #e4e4e4;
    --row-b: #eeeeee;
    --head-grey: #bdbdbd;
  }
  * { box-sizing: border-box; margin: 0; padding: 0; }
  html, body { width: 1200px; height: 941px; overflow: hidden; }
  body { background: var(--stage); font-family: "Montserrat", sans-serif; position: relative; }

  .page { position: absolute; top: 124px; width: 500px; height: 707px; background: var(--paper); overflow: hidden; box-shadow: 0 4px 14px rgba(0,0,0,.25); }
  .page--front { left: 82px; }
  .page--back { left: 618px; background: radial-gradient(#ececec 1px, transparent 1.2px) 0 0/7px 7px, #fbfbfb; }

  .layer { position: absolute; left: 0; top: 0; }

  .brand { position: absolute; width: 210px; text-align: center; color: var(--brand-blue); font-family: "Montserrat", sans-serif; line-height: 1; white-space: nowrap; }
  .brand__name { display: block; font-size: 30px; font-weight: 900; letter-spacing: -0.5px; }
  .brand__tag { display: block; font-size: 10.5px; font-weight: 600; letter-spacing: .1px; margin-top: 8px; }
  .page--front .brand { left: 229px; top: 22px; }
  .page--back .brand { left: 145px; top: 32px; }

  .pill { position: absolute; left: 0; height: 23px; background: var(--pill-grey); border: 2px solid #555; border-left: none; border-radius: 0 14px 14px 0; font-weight: 800; font-size: 14px; color: #2a2a2a; padding-left: 20px; line-height: 19px; white-space: nowrap; }
  .pill--about { top: 320px; width: 111px; }
  .pill--services { top: 520px; width: 146px; }

  .about__heading { position: absolute; left: 21px; top: 350px; width: 230px; color: #fff; font-weight: 900; font-size: 15.5px; line-height: 19px; }
  .about__heading span { font-weight: 400; }
  .about__text { position: absolute; left: 21px; top: 411px; width: 225px; color: #fff; font-weight: 500; font-size: 10px; line-height: 14px; }

  .services { position: absolute; left: 21px; top: 555px; list-style: none; color: #fff; font-size: 9.5px; font-weight: 500; }
  .services li { height: 18px; display: flex; align-items: center; gap: 8px; white-space: nowrap; }
  .services li::before { content: ""; width: 11px; height: 11px; border-radius: 50%; background: #d9e3ef; border: 1px solid #fff; }

  .headline { position: absolute; right: 21px; top: 312px; text-align: right; font-family: "Anton", sans-serif; font-weight: 400; color: var(--navy); font-size: 26px; line-height: 29px; white-space: nowrap; }
  .subline { position: absolute; right: 21px; top: 372px; text-align: right; color: #333; font-size: 16px; line-height: 20px; white-space: nowrap; }
  .cta { position: absolute; right: 21px; top: 456px; text-align: right; font-weight: 800; font-size: 16px; line-height: 19px; white-space: nowrap; }
  .cta__top { display: block; color: var(--pink); }
  .cta__bottom { display: block; color: var(--navy); }
  .quote-btn { position: absolute; right: 21px; top: 497px; width: 118px; height: 16px; border-radius: 8px; background: var(--pink); color: #fff; font-size: 9px; font-weight: 800; text-align: center; line-height: 16px; letter-spacing: .3px; }

  .contacts { position: absolute; right: 20px; top: 523px; text-align: right; list-style: none; font-size: 11px; line-height: 15.8px; color: var(--deep-blue); white-space: nowrap; }
  .contacts b { color: #111; font-weight: 800; }
  .contacts .web b, .contacts .mail b { color: var(--deep-blue); }
  .dot { display: inline-block; width: 8px; height: 8px; border: 1px solid #7a4fa0; border-radius: 50%; margin-right: 3px; vertical-align: -0.5px; }

  .follow { position: absolute; right: 22px; top: 587px; display: flex; align-items: center; gap: 4px; color: var(--pink); font-size: 9.5px; font-weight: 700; white-space: nowrap; }
  .follow span { margin-right: 3px; }
  .social { width: 13px; height: 13px; border-radius: 50%; }
  .social--a { background: #3b5b9a; }
  .social--b { background: #d2307a; }
  .social--c { background: #2ea3e6; }

  .front-footer { position: absolute; left: 0; top: 660px; width: 500px; text-align: center; color: #fff; }
  .front-footer__title { color: var(--sky); font-weight: 800; font-size: 10.5px; }
  .front-footer__text { font-size: 6.2px; line-height: 9.5px; margin-top: 2px; }

  .price-table { position: absolute; left: 47px; top: 107px; width: 406px; border-collapse: collapse; table-layout: fixed; font-size: 10.5px; color: #333; }
  .price-table col.item { width: 199px; }
  .price-table col.price { width: 104px; }
  .price-table th, .price-table td { height: 24px; text-align: center; padding: 0; white-space: nowrap; }
  .price-table thead th { background: var(--head-grey); font-weight: 500; font-size: 12.5px; color: #222; }
  .price-table thead th:first-child { background: #b3b3b3; }
  .price-table thead th + th { background: #d9d9d9; }
  .price-table tbody tr td { background: var(--row-a); }
  .price-table tbody tr:nth-child(even) td { background: var(--row-b); }
  .price-table td:first-child { background: #dcdcdc !important; }
  .price-table tr.band td { background: var(--brand-blue) !important; color: #fff; font-size: 12.5px; font-weight: 500; border-top: 1px solid #fff; }

  .back-footer { position: absolute; left: 0; top: 677px; width: 500px; text-align: center; color: #fff; font-size: 10px; font-weight: 500; white-space: nowrap; }
  .back-footer b { color: var(--sky); font-weight: 800; }
  .back-footer .dot { border-color: #cccccc; }
</style>
</head>
<body>

<section class="page page--front">
  <svg class="layer" width="500" height="707" viewBox="0 0 500 707" aria-hidden="true">
    <path d="M0 284 L237 284 C262 400 272 520 272 650 L0 660 Z" fill="var(--brand-blue)"/>
    <path d="M0 284 L237 284 C262 400 272 520 272 650 L200 652 C215 520 160 380 0 330 Z" fill="var(--deep-blue)" opacity=".35"/>
    <path d="M0 672 Q250 628 500 672 L500 707 L0 707 Z" fill="var(--charcoal)"/>
    <path d="M0 668 Q250 622 500 668" fill="none" stroke="#b5b5b5" stroke-width="3"/>
  </svg>

  <svg class="layer" width="500" height="290" viewBox="0 0 500 290" role="img" aria-label="Photo of a window cleaner wiping glass with a squeegee">
    <defs>
      <linearGradient id="photoTone" x1="0" y1="0" x2="1" y2="1">
        <stop offset="0" stop-color="#b9d3ea"/>
        <stop offset=".55" stop-color="#e3e8ee"/>
        <stop offset="1" stop-color="#c9ced4"/>
      </linearGradient>
    </defs>
    <path d="M0 0 L62 0 C110 70 190 104 278 104 C380 104 450 90 500 74 L500 254 C420 262 320 270 237 284 L0 284 Z" fill="url(#photoTone)"/>
    <path d="M62 0 C110 70 190 104 278 104" fill="none" stroke="var(--deep-blue)" stroke-width="9"/>
    <path d="M278 106 C380 106 450 92 500 76" fill="none" stroke="#bdbdbd" stroke-width="4"/>
    <path d="M237 286 C320 272 420 262 500 256" fill="none" stroke="#c3c3c3" stroke-width="4"/>
  </svg>

  <svg class="layer" width="160" height="320" viewBox="0 0 160 320" role="img" aria-label="Photo of gloved hands clearing a roof gutter">
    <circle cx="73" cy="227" r="77" fill="#2b2b2b"/>
    <circle cx="73" cy="227" r="73" fill="#5f6e68"/>
  </svg>

  <div class="brand">
    <span class="brand__name">LUNAR SWEEP</span>
    <span class="brand__tag">CLEANING &amp; MAINTENANCE LTD</span>
  </div>

  <div class="pill pill--about">ABOUT US</div>
  <h2 class="about__heading">RESIDENTIAL AND COMMERCIAL WINDOW CLEANING <span>IN ESSEX.</span></h2>
  <p class="about__text">Lunar Sweep Ltd have been cleaning windows for commercial and residential properties throughout Hutton, Shenfield and the surrounding areas since 1999. We cover most towns in Essex including Brentwood, Chelmsford, Romford, Loughton and Billericay.</p>

  <div class="pill pill--services">OUR SERVICES</div>
  <ul class="services">
    <li>Window Cleaning</li>
    <li>Conservatory Cleaning</li>
    <li>Pressure washing</li>
    <li>Gutter Cleaning</li>
    <li>Fascia &amp; Soffit’s cleaning</li>
  </ul>

  <h1 class="headline">RELIABLE WINDOW<br>CLEANING SERVICES</h1>
  <p class="subline">For residential and<br>commercial customers<br>in and around Essex</p>

  <p class="cta"><span class="cta__top">READY TO BOOK</span><span class="cta__bottom">WINDOW CLEANING</span></p>
  <div class="quote-btn">REQUEST TO QUOTE</div>

  <ul class="contacts">
    <li><span class="dot"></span>Office Number: <b>01394528160</b></li>
    <li><span class="dot"></span>Mobil Number: <b>07821563047</b></li>
    <li class="web"><span class="dot"></span><b>lunarsweep</b>.ltd</li>
    <li class="mail"><span class="dot"></span><b>lunarsweep</b>@postmerin.co.uk</li>
  </ul>

  <div class="follow"><span>Follow Us On</span><i class="social social--a"></i><i class="social social--b"></i><i class="social social--c"></i></div>

  <div class="front-footer">
    <p class="front-footer__title">We have got you covered</p>
    <p class="front-footer__text">Lunar Sweep offer a range of professional exterior cleaning services across Essex.<br>For both domestic and commercial clients a like.</p>
  </div>
</section>

<section class="page page--back">
  <svg class="layer" width="500" height="707" viewBox="0 0 500 707" aria-hidden="true">
    <path d="M0 672 Q250 626 500 672 L500 707 L0 707 Z" fill="var(--charcoal)"/>
    <path d="M0 666 Q250 620 500 666" fill="none" stroke="#bcbcbc" stroke-width="3"/>
  </svg>

  <div class="brand">
    <span class="brand__name">LUNAR SWEEP</span>
    <span class="brand__tag">CLEANING &amp; MAINTENANCE LTD</span>
  </div>

  <table class="price-table">
    <colgroup><col class="item"><col class="price"><col class="price"></colgroup>
    <thead><tr><th>Lorem ipsum dolor</th><th>Lorem ipsum</th><th>Lorem ipsum</th></tr></thead>
    <tbody>
      <tr><td>Lorem ipsum dolor</td><td>$160.00</td><td>$400.00</td></tr>
      <tr><td>Lorem ipsum dolor</td><td>$180.00</td><td>$420.00</td></tr>
      <tr><td>Lorem ipsum dolor</td><td>$250.00</td><td>$900.00</td></tr>
      <tr><td>Lorem ipsum dolor</td><td>$250.00</td><td>$ $900.00</td></tr>
      <tr><td>Lorem ipsum dolor</td><td>$350.00</td><td>$1,400.00</td></tr>
      <tr class="band"><td colspan="3">Window Cleaning</td></tr>
      <tr><td>Lorem ipsum dolor</td><td>$280.00</td><td>$1,150.00</td></tr>
      <tr><td>Lorem ipsum dolor</td><td>$280.00</td><td>$1,150.00</td></tr>
      <tr><td>Lorem ipsum dolor</td><td>$350.00</td><td>$1,350.00</td></tr>
      <tr><td>Lorem ipsum dolor</td><td>$450.00</td><td>$1,700.00</td></tr>
      <tr><td>Lorem ipsum dolor</td><td>$490.00</td><td>$1,900.00</td></tr>
      <tr><td>Lorem ipsum dolor</td><td>$600.00</td><td>$2,600.00</td></tr>
      <tr class="band"><td colspan="3">Pressure washing</td></tr>
      <tr><td>Lorem ipsum dolor</td><td>$200.00</td><td>$500.00</td></tr>
      <tr><td>Lorem ipsum dolor</td><td>$250.00</td><td>$700.00</td></tr>
      <tr><td>Lorem ipsum dolor</td><td>$180.00</td><td>$500.00</td></tr>
      <tr class="band"><td colspan="3">Gutter Cleaning</td></tr>
      <tr><td>Lorem ipsum dolor</td><td>$330.00</td><td>$1,100.00</td></tr>
      <tr><td>Lorem ipsum dolor</td><td>$330.00</td><td>$1,100.00</td></tr>
      <tr><td>Lorem ipsum dolor</td><td>$160.00</td><td>$600.00</td></tr>
    </tbody>
  </table>

  <p class="back-footer"><span class="dot"></span>Office Number: <b>01394528160</b> | <span class="dot"></span>Mobil Number: <b>07821563047</b> | <span class="dot"></span><b>lunarsweep</b>.ltd</p>
</section>

</body>
</html>
```